TRELLWICK Construction Group business card for distribution

A business card detailing our services, with our phone number and email address.
- Groundworks / Foundations / Drainage
- Landscaping / Hard Landscaping / Patios / Decking
- Fencing
The card should include company logo and be in the same colours.

Target Market(s)
Domestic Houses
Industry/Entity Type
Construction
Contact Information for Business Card
Phone Number - 07931 258 904 / 07713829516. Email address: trellgroup@stonevane-mail.com
Font styles to use
Serif
Sans Serif
Colors
F0912C
F2A743
F7CA91
FBE8D2
FDF5EE
Requirements
Must have
- Contact numbers. Photos of past work. Company Logo

Nice to have
- Company Logo

```html
<!DOCTYPE html>
<html lang="en">
<head>
<meta charset="utf-8">
<title>TRELLWICK Construction Group – Business Card</title>
<link rel="stylesheet" href="https://fonts.googleapis.com/css2?family=Montserrat:wght@700&family=Roboto:wght@400;500&display=swap">
<style>
  :root {
    --orange: #f0912c;
    --orange-deep: #f07d1a;
    --charcoal: #2b2b2b;
    --charcoal-dark: #1d1d1d;
    --steel: #8a8a8a;
    --white: #ffffff;
    --ink: #4a4a4a;
    --backdrop: #1a1b1d;
  }
  * { box-sizing: border-box; margin: 0; padding: 0; }
  html, body { width: 1200px; height: 840px; overflow: hidden; }
  body {
    background: var(--backdrop);
    font-family: "Roboto", Arial, sans-serif;
    display: flex;
    flex-direction: column;
    align-items: center;
    justify-content: center;
    gap: 40px;
  }
  .card {
    position: relative;
    width: 620px;
    height: 354px;
    border-radius: 22px;
    overflow: hidden;
    box-shadow: 0 4px 0 var(--orange-deep);
  }

  /* Back side */
  .card--back { background: var(--charcoal); }
  .card__bands { position: absolute; inset: 0; width: 100%; height: 100%; }
  .brand {
    position: absolute;
    font-family: "Montserrat", Arial, sans-serif;
    font-weight: 700;
    display: flex;
    align-items: center;
    gap: 12px;
  }
  .brand__mark { width: 22px; height: 22px; background: var(--orange); flex: none; }
  .brand__name { line-height: 1.05; }
  .brand__name span { display: block; }
  .card--back .brand { top: 34px; right: 40px; color: var(--white); }
  .card--back .brand__name span:first-child { font-size: 38px; letter-spacing: 1px; }
  .card--back .brand__name span:last-child { font-size: 11.5px; letter-spacing: 1.6px; }

  .services {
    position: absolute;
    right: 40px;
    top: 128px;
    text-align: right;
    list-style: none;
  }
  .services__title {
    color: var(--orange);
    font-weight: 500;
    font-size: 18px;
    text-transform: uppercase;
    margin-bottom: 4px;
  }
  .services li {
    color: var(--white);
    font-size: 17px;
    line-height: 23px;
  }
  .services li::after {
    content: "";
    display: inline-block;
    width: 7px; height: 7px;
    border-radius: 50%;
    background: var(--orange);
    margin-left: 8px;
    vertical-align: middle;
  }

  /* Front side */
  .card--front { background: var(--white); }
  .card--front .brand { left: 44px; top: 150px; color: var(--charcoal); }
  .card--front .brand__name span:first-child { font-size: 34px; letter-spacing: 1px; }
  .card--front .brand__name span:last-child { font-size: 10.5px; letter-spacing: 1.5px; }
  .divider {
    position: absolute;
    left: 318px;
    top: 110px;
    width: 1px;
    height: 130px;
    background: var(--steel);
  }
  .contact { position: absolute; left: 342px; top: 104px; }
  .contact__name {
    color: var(--orange);
    font-weight: 500;
    font-size: 25px;
    text-transform: uppercase;
    letter-spacing: 0.3px;
  }
  .contact__role { color: var(--ink); font-size: 18px; margin-bottom: 14px; }
  .contact__line {
    display: flex; align-items: center; gap: 8px;
    color: var(--ink); font-size: 16.5px; line-height: 26px;
  }
  .contact__icon { width: 16px; height: 16px; flex: none; }
</style>
</head>
<body>

  <section class="card card--back" aria-label="Card back: services">
    <svg class="card__bands" viewBox="0 0 620 354" preserveAspectRatio="none" aria-hidden="true">
      <defs>
        <linearGradient id="steelSheen" x1="0" y1="0" x2="1" y2="0.3">
          <stop offset="0" stop-color="#151515"/>
          <stop offset="0.45" stop-color="#3a3a3a"/>
          <stop offset="0.6" stop-color="#8a8a8a"/>
          <stop offset="1" stop-color="#3a3a3a"/>
        </linearGradient>
      </defs>
      <polygon points="0,0 250,0 250,70 0,150" fill="#1e1e1e"/>
      <polygon points="0,170 90,150 330,250 420,250 320,354 0,354" fill="url(#steelSheen)"/>
      <polygon points="0,150 250,70 255,74 0,160" fill="#333333"/>
    </svg>

    <div class="brand">
      <div class="brand__name"><span>TRELLWICK</span><span>CONSTRUCTION GROUP LTD</span></div>
      <div class="brand__mark"></div>
    </div>

    <ul class="services">
      <li class="services__title">Our Services</li>
      <li>Groundworks</li>
      <li>Foundations</li>
      <li>Drainage</li>
      <li>Landscaping</li>
      <li>Hard Landscaping</li>
      <li>Patios</li>
      <li>Decking</li>
      <li>Fencing</li>
    </ul>
  </section>

  <section class="card card--front" aria-label="Card front: contact">
    <div class="brand">
      <div class="brand__mark"></div>
      <div class="brand__name"><span>TRELLWICK</span><span>CONSTRUCTION GROUP LTD</span></div>
    </div>

    <div class="divider"></div>

    <div class="contact">
      <p class="contact__name">Daniel Harwood</p>
      <p class="contact__role">Manager</p>
      <p class="contact__line">
        <svg class="contact__icon" viewBox="0 0 24 24" aria-hidden="true"><path fill="#f0912c" d="M6.6 10.8a15.1 15.1 0 0 0 6.6 6.6l2.2-2.2c.3-.3.7-.4 1-.2 1.1.4 2.3.6 3.6.6.6 0 1 .4 1 1V20c0 .6-.4 1-1 1A17 17 0 0 1 3 4c0-.6.4-1 1-1h3.5c.6 0 1 .4 1 1 0 1.3.2 2.5.6 3.6.1.3 0 .7-.2 1z"/></svg>
        07931 258 904
      </p>
      <p class="contact__line">
        <svg class="contact__icon" viewBox="0 0 24 24" aria-hidden="true"><path fill="#f0912c" d="M6.6 10.8a15.1 15.1 0 0 0 6.6 6.6l2.2-2.2c.3-.3.7-.4 1-.2 1.1.4 2.3.6 3.6.6.6 0 1 .4 1 1V20c0 .6-.4 1-1 1A17 17 0 0 1 3 4c0-.6.4-1 1-1h3.5c.6 0 1 .4 1 1 0 1.3.2 2.5.6 3.6.1.3 0 .7-.2 1z"/></svg>
        07713829516
      </p>
      <p class="contact__line">
        <svg class="contact__icon" viewBox="0 0 24 24" aria-hidden="true"><path fill="#f0912c" d="M2 9l10-7 10 7v11a1 1 0 0 1-1 1H3a1 1 0 0 1-1-1zm2 1.2V19h16v-8.8l-8 5.3z"/></svg>
        trellgroup@stonevane-mail.com
      </p>
    </div>
  </section>

</body>
</html>
```